My company Tilt Foundry, founded in 2004 and based in downtown Brooklyn, NY, is a design firm specializing in furniture and residential projects, primarily apartments in New York City but also houses in the New York area. The built projects are distinctly modern, and the furniture (large wooden constructions that hold books and objects) border on sculpture. I also do a fair amount of photography and drawing, so my ideal client is someone who collects current art and photography and wants a space commensurate with that interest. The purpose of the website is twofold. First, to attract a clientele for residential projects who have a strong interest in contemporary art, and secondly, to develop a platform for selling my furniture on a made-to-order basis. The website, and especially the landing page, should visualize my preference for raw materials-construction lumber, plywood, concrete, exposed bolts and screws, etc. I like bold colors, graffiti, accidental marks, and all species of imperfection. Slick and ultra-stylized is not my thing. With regard to typeface, I like it simple and unadorned, but assertive, and handwritten is an option as long as it is bold. The landing page could simply be a background featuring one of the above preferences, with TILT FOUNDRY overlaid in black (or colored?) type and a small 'enter' button to an index page, but I'm open to suggestions. See additional directions below...Thanks!

Target Market(s)

People interested in contemporary art, photography, architecture and design

Industry/Entity Type

Residential

Requirements
Must have
• All I would like to see initially is a landing page and index page. The landing page as stated above should have a material background-see attached photos (any will do) with the company name and enter button.
The index page should include the following categories with links to be designed later: About, Portfolio, Purchase Furniture, Contact. Use a second material background from the attached photos for the index page. NOTE: please use the concrete slab photo on one of the pages, the other page can have either plywood or carboard, whichever works best for your design. If you want to replicate the ply or cardboard in a grid that's fine too
Should not have
• Since I take an ipad when I meet with clients the site cannot utilize Flash. Also no sound.

```html
<!DOCTYPE html>
<html lang="en">
<head>
<meta charset="utf-8">
<title>Tilt Foundry — About</title>
<link rel="stylesheet" href="https://fonts.googleapis.com/css2?family=Jost:wght@400;500;700&family=Cabin:wght@400&display=swap">
<style>
  :root {
    --wood-light: #ecd69a;
    --wood-mid: #e0bb72;
    --wood-deep: #c98f4a;
    --brand-blue: #1a8ccd;
    --heading-teal: #0d4f70;
    --ink: #1a140c;
    --veil: rgba(255, 250, 235, 0.14);
    --nav-active: rgba(255, 250, 235, 0.28);
  }
  * { margin: 0; padding: 0; box-sizing: border-box; }
  html, body { width: 1200px; height: 900px; overflow: hidden; }
  body { position: relative; font-family: "Cabin", sans-serif; color: var(--ink); }

  .plywood-surface {
    position: absolute; inset: 0;
    background:
      radial-gradient(ellipse 260px 420px at 130px 640px, rgba(201,143,74,0.55), transparent 70%),
      radial-gradient(ellipse 200px 500px at 700px 300px, rgba(201,143,74,0.35), transparent 70%),
      radial-gradient(ellipse 220px 480px at 1000px 650px, rgba(201,143,74,0.4), transparent 70%),
      linear-gradient(100deg, var(--wood-light) 0%, var(--wood-mid) 45%, var(--wood-light) 70%, var(--wood-mid) 100%);
  }
  .content-veil {
    position: absolute; left: 516px; top: 0; width: 684px; height: 900px;
    background: var(--veil);
  }

  .brand {
    position: absolute; right: 775px; top: 178px;
    text-align: right;
    font-family: "Jost", sans-serif; font-weight: 700;
    color: var(--brand-blue);
    line-height: 0.9;
    letter-spacing: -1px;
  }
  .brand-line-one { display: block; font-size: 74px; }
  .brand-line-two { display: block; font-size: 56px; }

  .main-nav {
    position: absolute; left: 360px; top: 378px; width: 156px;
    list-style: none;
    font-family: "Jost", sans-serif; font-weight: 400;
    font-size: 21px; letter-spacing: 1.5px;
  }
  .main-nav li { height: 58.5px; }
  .main-nav a {
    display: block; height: 58px; line-height: 60px;
    padding-right: 47px; text-align: right;
    color: var(--ink); text-decoration: none; white-space: nowrap;
  }
  .main-nav .is-active a { background: var(--nav-active); }
  .main-nav li:not(.is-active) a { margin-left: -40px; }

  .page-title {
    position: absolute; right: 86px; top: 276px;
    font-family: "Jost", sans-serif; font-weight: 700;
    font-size: 52px; letter-spacing: 0.5px;
    color: var(--heading-teal);
    text-shadow: 2px 2px 2px rgba(0,0,0,0.35);
  }

  .about-copy {
    position: absolute; left: 592px; top: 387px; width: 555px;
    font-size: 13.6px; line-height: 20px;
  }
  .about-copy p + p { margin-top: 20px; }
</style>
</head>
<body>
  <div class="plywood-surface" role="img" aria-label="Plywood sheet with warm honey-coloured wood grain"></div>
  <div class="content-veil"></div>

  <header class="brand" aria-label="Tilt Foundry">
    <span class="brand-line-one">TILT</span>
    <span class="brand-line-two">FOUNDRY</span>
  </header>

  <nav>
    <ul class="main-nav">
      <li class="is-active"><a href="#about">ABOUT</a></li>
      <li><a href="#portfolio">PORTFOLIO</a></li>
      <li><a href="#purchase">PURCHASE</a></li>
      <li><a href="#contact">CONTACT</a></li>
    </ul>
  </nav>

  <main>
    <h1 class="page-title">ABOUT</h1>
    <section class="about-copy">
      <p>Lorem ipsum dolor sit amet, consectetur adipiscing elit. Vestibulum sed varius diam. Donec varius feugiat tortor, nec accumsan tortor dictum quis. Sed non risus ac magna suscipit mollis. Nam tempor lectus vitae nibh vehicula quis rhoncus elit accumsan.</p>
      <p>Fusce nisi quam, sagittis sit amet malesuada ac, pharetra a neque. Integer sagittis, sapien vel posuere pharetra, elit elit lacinia enim, in pulvinar erat velit a neque. Etiam massa dolor, fermentum ac posuere sed, aliquet ut velit. Nulla est nibh, dignissim eget rhoncus et, tincidunt eget nibh. Integer eget ante sit amet felis mattis tincidunt quis eget justo.</p>
      <p>Donec fermentum, libero a rhoncus ultricies, metus dolor lobortis nulla, in rutrum eros mauris at mi. Curabitur ullamcorper bibendum tellus, vel consectetur nulla gravida a. Nam tortor odio, venenatis eget commodo imperdiet, porta vel felis. Vivamus nec commodo dolor. Suspendisse tempus fringilla nisl, quis venenatis lectus facilisis eget. Lorem ipsum dolor sit amet, consectetur adipiscing elit. Sed quis turpis sapien.</p>
      <p>Vestibulum ante ipsum primis in faucibus orci luctus et ultrices posuere cubilia Curae; Vestibulum mi ante, tempor ac vulputate vitae, posuere sit amet magna. Vestibulum id ipsum a tellus faucibus sodales et ac magna. Etiam mollis placerat metus, vel gravida dui hendrerit ut. In purus mi, semper eu eleifend nec, hendrerit nec ligula. Vestibulum arcu libero, porta non sagittis a, tempor non ante.</p>
    </section>
  </main>
</body>
</html>
```